" é um consultório particular de atendimento médico na área de otorrinolaringologia , sou formada há 30 anos mas ano tenho um nome de marca , apenas meu nome profissional. tenho uma logo mas muito fraca e nela não tem a informação do que faço e qual minha especialidade ... e nem meu nome "

```html
<!DOCTYPE html>
<html lang="pt-BR">
<head>
<meta charset="utf-8">
<title>Cartão digital – Dra. Helena Marques Duarte</title>
<link rel="stylesheet" href="https://fonts.googleapis.com/css2?family=Cormorant+Garamond:ital,wght@0,600;1,600&family=Roboto:wght@400;500&display=swap">
<style>
  :root{
    --page:#eeedf6;
    --green-dark:#1f2c22;
    --green:#34473a;
    --green-light:#4a5f4f;
    --gold:#c9a96a;
    --gold-light:#ecd9a8;
    --gold-deep:#a8874a;
    --white:#ffffff;
    --ink:#1f2c22;
    --text-light:#e9ece6;
  }
  *{margin:0;padding:0;box-sizing:border-box}
  html,body{width:1200px;height:1200px;overflow:hidden;background:var(--page)}
  .card{
    position:absolute;left:343px;top:192px;width:439px;height:768px;
    background:radial-gradient(ellipse at 50% 55%,var(--green-light) 0%,var(--green) 45%,var(--green-dark) 100%);
    overflow:hidden;box-shadow:0 2px 8px rgba(0,0,0,.12);
    font-family:"Roboto",Arial,sans-serif;color:var(--text-light);
  }
  .card-header{position:absolute;left:0;top:0;width:439px;height:340px}
  .brand{position:absolute;left:0;top:70px;width:439px;text-align:center}
  .brand-mark{display:inline-flex;align-items:center;gap:10px;
    font-family:"Cormorant Garamond",Georgia,serif;font-weight:600;font-size:52px;
    color:var(--ink);letter-spacing:4px}
  .brand-mark .dot{width:22px;height:22px;border-radius:50%;background:var(--ink)}
  .doctor-name{position:absolute;left:0;top:238px;width:439px;text-align:center;
    font-family:"Cormorant Garamond",Georgia,serif;font-style:italic;font-weight:600;
    font-size:22px;color:var(--ink)}
  .doctor-specialty{position:absolute;left:0;top:266px;width:439px;text-align:center;
    font-size:8px;letter-spacing:3px;color:var(--ink)}
  .doctor-crm{position:absolute;left:0;top:280px;width:439px;text-align:center;
    font-size:9px;color:var(--ink)}
  .section-title{position:absolute;left:0;top:344px;width:439px;text-align:center;
    font-size:17px;letter-spacing:5px;font-weight:400}
  .watermark{position:absolute;left:0;top:500px;width:439px;text-align:center;
    font-family:"Cormorant Garamond",Georgia,serif;font-weight:600;font-size:90px;
    color:rgba(0,0,0,.12);letter-spacing:6px}
  .actions{position:absolute;left:58px;top:384px;width:323px;
    display:grid;grid-template-columns:repeat(3,1fr);row-gap:34px}
  .action{display:flex;flex-direction:column;align-items:center;gap:14px}
  .action-icon{width:67px;height:67px;border-radius:8px;
    background:linear-gradient(145deg,var(--gold-light),var(--gold) 55%,var(--gold-deep));
    display:flex;align-items:center;justify-content:center;
    box-shadow:0 3px 6px rgba(0,0,0,.35)}
  .action-icon svg{width:34px;height:34px}
  .action-label{font-size:14px;color:var(--text-light)}
  .cta{position:absolute;left:0;top:681px;width:439px;text-align:center;font-size:17px}
  .address{position:absolute;left:0;top:718px;width:439px;text-align:center;
    font-size:11.5px;line-height:19px}
</style>
</head>
<body>
<main class="card">
  <svg class="card-header" viewBox="0 0 439 340" aria-hidden="true">
    <defs>
      <linearGradient id="goldBand" x1="0" x2="1">
        <stop offset="0" stop-color="#a8874a"/>
        <stop offset=".5" stop-color="#ecd9a8"/>
        <stop offset="1" stop-color="#a8874a"/>
      </linearGradient>
    </defs>
    <path d="M0 0H439V320C330 296 150 300 0 332Z" fill="url(#goldBand)"/>
    <path d="M0 52C140 22 300 20 439 40V312C330 290 150 294 0 322Z" fill="#ffffff"/>
    <path d="M0 0H439V32C300 10 140 14 0 46Z" fill="#1f2c22"/>
  </svg>

  <div class="brand"><span class="brand-mark"><span class="dot"></span>HMD</span></div>
  <h1 class="doctor-name">Dra. Helena Marques Duarte</h1>
  <p class="doctor-specialty">OTORRINOLARINGOLOGIA</p>
  <p class="doctor-crm">CRM-MG 40571</p>

  <h2 class="section-title">OTORRINOLARINGOLOGIA</h2>
  <div class="watermark" aria-hidden="true">HMD</div>

  <nav class="actions">
    <div class="action">
      <span class="action-icon"><svg viewBox="0 0 24 24"><path fill="#1f2c22" d="M6.6 10.8a15.1 15.1 0 0 0 6.6 6.6l2.2-2.2c.3-.3.7-.4 1-.2 1.1.4 2.3.6 3.6.6.6 0 1 .4 1 1V20c0 .6-.4 1-1 1A17 17 0 0 1 3 4c0-.6.4-1 1-1h3.5c.6 0 1 .4 1 1 0 1.3.2 2.5.6 3.6.1.3 0 .7-.2 1z"/></svg></span>
      <span class="action-label">Telefone Fixo</span>
    </div>
    <div class="action">
      <span class="action-icon"><svg viewBox="0 0 24 24"><circle cx="12" cy="12" r="9" fill="#1f2c22"/></svg></span>
      <span class="action-label">Secretária</span>
    </div>
    <div class="action">
      <span class="action-icon"><svg viewBox="0 0 24 24"><rect x="3" y="3" width="18" height="18" rx="4" fill="#1f2c22"/></svg></span>
      <span class="action-label">Rede social</span>
    </div>
    <div class="action">
      <span class="action-icon"><svg viewBox="0 0 24 24"><circle cx="12" cy="12" r="9" fill="#1f2c22"/></svg></span>
      <span class="action-label">Dra. Helena</span>
    </div>
    <div class="action">
      <span class="action-icon"><svg viewBox="0 0 24 24"><rect x="2" y="5" width="20" height="14" rx="1" fill="#1f2c22"/><path d="M2.5 5.5 12 13l9.5-7.5M2.5 18.5 9 11.5M21.5 18.5 15 11.5" stroke="#d9bf85" stroke-width="1.2" fill="none"/></svg></span>
      <span class="action-label">E-mail</span>
    </div>
    <div class="action">
      <span class="action-icon"><svg viewBox="0 0 24 24"><path fill="#1f2c22" d="M12 2a7 7 0 0 0-7 7c0 5.2 7 13 7 13s7-7.8 7-13a7 7 0 0 0-7-7zm0 9.5A2.5 2.5 0 1 1 12 6.5a2.5 2.5 0 0 1 0 5z"/></svg></span>
      <span class="action-label">Endereço</span>
    </div>
  </nav>

  <p class="cta">Clique nos ícones para interagir</p>
  <p class="address">Endereço Rua das Acácias, 250 | 302 ,<br>Bairro Jardim Aurora CEP: 30100-450 &nbsp;| BH-MG</p>
</main>
</body>
</html>
```